Lumen Ridge Puzzles Business Cards
Two-sided business cards
Professional
Pim Varlotte
Founder, KORV Fellow, Brellaquin MVP
pim@lumenridgepuzzles.example
www.lumenridgepuzzles.example
GPG Fingerprint: A2D1 5B09 F6C3 17E4 8D2A 40BC 9E71 3F58 C046
Logo to Use for Business Cards

```html
<!DOCTYPE html>
<html lang="en">
<head>
<meta charset="utf-8">
<title>Lumen Ridge Puzzles — Stationery</title>
<link href="https://fonts.googleapis.com/css2?family=Roboto:wght@400;700&display=swap" rel="stylesheet">
<style>
  :root{
    --backdrop:#a7a7a7;
    --paper:#ffffff;
    --blue-deep:#1546a8;
    --blue-bright:#3a7be0;
    --ink-dark:#1b1b1b;
    --steel:#8a8f96;
    --text:#333a44;
    --mark-faint:#e6ebf3;
  }
  *{box-sizing:border-box;margin:0;padding:0}
  html,body{width:1200px;height:809px;overflow:hidden;background:var(--backdrop);font-family:'Roboto',sans-serif;color:var(--text)}
  .canvas{position:relative;width:1200px;height:809px}
  .sheet{position:absolute;background:var(--paper);overflow:hidden;box-shadow:0 1px 3px rgba(0,0,0,.25)}
  .band{position:absolute;left:0;width:100%;display:block}
  .brand{position:absolute;display:flex;align-items:center;gap:5px;font-weight:700;color:var(--blue-deep);white-space:nowrap;letter-spacing:.02em}
  .brand-dot{border-radius:50%;background:var(--blue-deep);flex:none}
  .faint-mark{position:absolute;display:flex;align-items:center;justify-content:center;border-radius:50%;border:3px solid var(--mark-faint);color:var(--mark-faint);font-weight:700;text-align:center;line-height:1.1}
  .fine{position:absolute;font-size:5px;line-height:8px;color:var(--text);white-space:nowrap}
  .band-url{position:absolute;font-size:5px;color:#fff;white-space:nowrap}

  /* letterhead */
  .letterhead{left:113px;top:67px;width:468px;height:634px}
  .letterhead .brand{left:62px;top:96px;font-size:10px}
  .letterhead .brand-dot{width:9px;height:9px}
  .letterhead .fine{left:38px;top:576px}
  .letterhead .faint-mark{right:26px;bottom:32px;width:72px;height:72px;font-size:8px}

  /* business cards */
  .card-front{left:24px;top:281px;width:204px;height:79px;background:radial-gradient(circle at 30% 30%,var(--blue-bright),var(--blue-deep) 80%)}
  .card-front .brand{left:12px;top:33px;font-size:10px;color:#fff}
  .card-front .brand-dot{width:9px;height:9px;background:#fff}
  .card-front .band-url{right:10px;bottom:8px}
  .card-back{left:24px;top:365px;width:204px;height:93px}
  .card-back .brand{left:12px;top:14px;font-size:9px}
  .card-back .brand-dot{width:8px;height:8px}
  .card-back .fine{left:10px;top:40px;font-size:4.2px;line-height:7px}

  /* open envelope */
  .envelope{left:619px;top:12px;width:555px;height:454px}
  .flap{position:absolute;left:14px;top:82px;width:527px;height:136px;border-radius:0 0 22px 22px;background:radial-gradient(ellipse at 55% 20%,var(--blue-bright),var(--blue-deep) 75%)}
  .fold{position:absolute;left:0;top:228px;width:100%;height:2px;background:#d7d9dd}
  .envelope .fine{left:92px;top:303px}

  /* window envelope */
  .dl-envelope{left:619px;top:504px;width:555px;height:259px}
  .dl-envelope .brand{left:46px;top:56px;font-size:10px}
  .dl-envelope .brand-dot{width:9px;height:9px}
  .dl-envelope .fine{left:46px;top:144px}
  .dl-envelope .faint-mark{right:18px;bottom:22px;width:62px;height:62px;font-size:7px}
</style>
</head>
<body>
<main class="canvas">
  <svg width="0" height="0" style="position:absolute">
    <defs>
      <linearGradient id="band-blue" x1="0" x2="1">
        <stop offset="0" stop-color="#2f6fd8"/>
        <stop offset="1" stop-color="#1546a8"/>
      </linearGradient>
      <symbol id="band" viewBox="0 0 100 10" preserveAspectRatio="none">
        <polygon points="0,0 74,0 70,10 0,10" fill="url(#band-blue)"/>
        <polygon points="74,0 92,0 88,10 70,10" fill="#1b1b1b"/>
        <polygon points="92,0 100,0 100,10 88,10" fill="#8a8f96"/>
      </symbol>
    </defs>
  </svg>

  <section class="sheet letterhead" aria-label="Letterhead">
    <svg class="band" style="top:0;height:9px"><use href="#band"/></svg>
    <div class="brand"><span class="brand-dot"></span>LUMEN RIDGE PUZZLES</div>
    <p class="fine">Phone: +1 555 0142<br>Studio 4, Ridge Lane<br>pim@lumenridgepuzzles.example</p>
    <div class="faint-mark">LUMEN<br>RIDGE</div>
    <svg class="band" style="bottom:0;height:11px"><use href="#band"/></svg>
    <span class="band-url" style="left:40px;bottom:2px">www.lumenridgepuzzles.example</span>
  </section>

  <section class="sheet card-front" aria-label="Business card front">
    <div class="brand"><span class="brand-dot"></span>LUMEN RIDGE PUZZLES</div>
    <span class="band-url">www.lumenridgepuzzles.example</span>
  </section>

  <section class="sheet card-back" aria-label="Business card back">
    <div class="brand"><span class="brand-dot"></span>LUMEN RIDGE PUZZLES</div>
    <p class="fine"><b>Pim Varlotte</b> | Founder, KORV Fellow, Brellaquin MVP<br>pim@lumenridgepuzzles.example<br>GPG: A2D1 5B09 F6C3 17E4 8D2A 40BC 9E71 3F58 C046</p>
    <svg class="band" style="bottom:0;height:8px"><use href="#band"/></svg>
  </section>

  <section class="sheet envelope" aria-label="Envelope, flap open">
    <div class="flap"></div>
    <div class="fold"></div>
    <p class="fine">www.lumenridgepuzzles.example</p>
  </section>

  <section class="sheet dl-envelope" aria-label="Envelope front">
    <svg class="band" style="top:14px;height:8px"><use href="#band"/></svg>
    <div class="brand"><span class="brand-dot"></span>LUMEN RIDGE PUZZLES</div>
    <p class="fine">Phone: +1 555 0142<br>Studio 4, Ridge Lane<br>pim@lumenridgepuzzles.example</p>
    <div class="faint-mark">LUMEN<br>RIDGE</div>
    <svg class="band" style="bottom:14px;height:8px"><use href="#band"/></svg>
  </section>
</main>
</body>
</html>
```